VANTO Brochure Design Project

I need a brochure for my new project management company.
the scope covers all engineering aspects of developments.
Green design is also included. so, I would like to see colours representing the industry and sustainability. soft colours really.
Hello, I'm attaching herewith the text, images, and the logo that i want to appear on the brochure
developers, investors, governments
Industry

```html
<!DOCTYPE html>
<html lang="en">
<head>
<meta charset="utf-8">
<title>VANTO Project Management Brochure</title>
<link href="https://fonts.googleapis.com/css2?family=Questrial&family=Montserrat:wght@600&display=swap" rel="stylesheet">
<style>
  :root{
    --navy:#1c2b6a;
    --navy-deep:#17235a;
    --sky:#5a8fd0;
    --ink:#23328a;
    --ink-strong:#1d2a7a;
    --tagline:#cdd7f0;
    --contact:#e3e9f7;
    --faint:rgba(70,95,170,.22);
    --stage:#eceef2;
  }
  *{margin:0;padding:0;box-sizing:border-box}
  html,body{width:1200px;height:807px;overflow:hidden;background:var(--stage)}
  body{font-family:"Questrial",sans-serif;position:relative}
  .brochure{position:absolute;left:38px;top:40px;width:1402px;height:908px;transform:scale(.8);transform-origin:0 0;box-shadow:0 6px 18px rgba(0,0,0,.25)}
  .panel{position:absolute;top:0;height:908px;overflow:hidden}
  .panel--back{left:0;width:702px;background:linear-gradient(180deg,var(--navy) 0%,var(--navy-deep) 100%)}
  .panel--front{left:702px;width:700px;background:linear-gradient(180deg,#1f2f70 0%,var(--navy) 60%,var(--navy-deep) 100%);border-left:1px solid rgba(255,255,255,.25)}
  .panel-art{position:absolute;left:0;top:0}
  .services{position:absolute;left:201px;top:306px;color:var(--ink)}
  .services__title{font-size:29px;font-weight:400;color:var(--ink-strong);margin-bottom:24px;line-height:1.2}
  .services__lead{font-family:"Montserrat",sans-serif;font-weight:600;font-size:17.5px;color:var(--ink-strong);margin-bottom:8px}
  .services__list{list-style:none}
  .services__list li{font-size:17.5px;line-height:29.8px;padding-left:18px;position:relative;white-space:nowrap}
  .services__list li::before{content:"";position:absolute;left:0;top:11px;width:9px;height:9px;border-radius:50%;background:radial-gradient(circle at 35% 35%,#c8ccd6,#4e5464)}
  .faint-word{position:absolute;left:112px;top:690px;font-size:140px;letter-spacing:22px;color:var(--faint);line-height:1}
  .faint-tag{position:absolute;left:24px;top:846px;font-size:38px;letter-spacing:10px;color:var(--faint);white-space:nowrap;line-height:1}
  .contact-mark{position:absolute;left:69px;top:773px;width:61px;text-align:center}
  .contact-mark__square{width:61px;height:61px;background:linear-gradient(135deg,#8fb8e6,#3e72bf)}
  .contact-mark__name{font-size:15px;color:var(--sky);letter-spacing:2px;margin-top:2px;line-height:1}
  .contact{position:absolute;left:139px;top:770px;border-left:1px solid rgba(255,255,255,.45);padding-left:8px;list-style:none}
  .contact li{font-size:12px;line-height:18.5px;color:var(--contact);display:flex;align-items:center;gap:5px}
  .contact svg{width:9px;height:9px;fill:none;stroke:#9fb7e6;stroke-width:1.4}
  .front-mark{position:absolute;left:115px;top:95px;width:110px;text-align:center}
  .front-mark__square{width:110px;height:110px;background:linear-gradient(135deg,#8fb8e6,#3e72bf)}
  .front-mark__name{font-size:27px;color:var(--sky);letter-spacing:4px;margin-top:4px;line-height:1}
  .front-mark__desc{font-size:8.5px;color:#566690;letter-spacing:1.6px;margin-top:4px;white-space:nowrap}
  .tagline{position:absolute;left:0;width:700px;top:720px;text-align:center;font-size:36px;color:var(--tagline);letter-spacing:.5px}
  .web-tab{position:absolute;left:430px;top:847px;width:270px;height:45px}
  .web-tab__text{position:absolute;left:70px;top:12px;font-size:17px;color:var(--ink-strong);display:flex;align-items:center;gap:6px}
  .web-tab__text svg{width:13px;height:13px;fill:none;stroke:#3e62b0;stroke-width:1.3}
  .fold-strip{position:absolute;left:0;top:892px;width:1402px;height:16px;background:linear-gradient(90deg,#1d55a8,#4f86cf 50%,#1d55a8)}
</style>
</head>
<body>
<div class="brochure">
  <section class="panel panel--back">
    <svg class="panel-art" width="702" height="908" viewBox="0 0 702 908">
      <defs>
        <radialGradient id="servicesGlow" cx="0.5" cy="0.62" r="0.62">
          <stop offset="0" stop-color="#ffffff"/>
          <stop offset="0.45" stop-color="#dbe7f7"/>
          <stop offset="1" stop-color="#5f92d3"/>
        </radialGradient>
        <linearGradient id="tabBlue" x1="0" x2="1">
          <stop offset="0" stop-color="#2e63b3"/><stop offset="1" stop-color="#1c4fa0"/>
        </linearGradient>
        <linearGradient id="towerTone" x1="0" x2="1"><stop offset="0" stop-color="#f4f5f7"/><stop offset="1" stop-color="#9aa2ad"/></linearGradient>
        <linearGradient id="resortTone" x1="0" x2="1"><stop offset="0" stop-color="#7f9b86"/><stop offset="1" stop-color="#c9b9a0"/></linearGradient>
        <linearGradient id="campusTone" x1="0" x2="1"><stop offset="0" stop-color="#6f9a6a"/><stop offset="1" stop-color="#c8c2b6"/></linearGradient>
      </defs>
      <rect x="27" y="22" width="650" height="620" fill="rgba(60,85,160,.18)"/>
      <polygon points="0,273 702,273 702,618 624,700 0,700" fill="url(#servicesGlow)"/>
      <polygon points="0,273 188,273 150,320 0,320" fill="url(#tabBlue)"/>
      <polygon points="15,255 93,124 264,124 264,255" fill="url(#towerTone)" role="img" aria-label="Photo of a glass and steel high-rise tower"/>
      <polygon points="227,255 274,175 302,124 476,124 476,165 405,255" fill="url(#resortTone)" role="img" aria-label="Photo of a palm-lined resort building with fountains"/>
      <polygon points="439,255 486,175 516,124 688,124 688,165 620,255" fill="url(#campusTone)" role="img" aria-label="Rendering of a green campus development"/>
    </svg>
    <div class="faint-word" aria-hidden="true">Vanto</div>
    <div class="faint-tag" aria-hidden="true">PROJECT MANAGEMENT</div>
    <div class="services">
      <h2 class="services__title">Our green services</h2>
      <p class="services__lead">Our green services include:</p>
      <ul class="services__list">
        <li>Terrava Strategy, Certification &amp; Management</li>
        <li>Ecolume Strategy, Certification &amp; Management</li>
        <li>Renewable Energy Feasibility</li>
        <li>Water Conservation Strategies</li>
        <li>Building Performance Assessments</li>
        <li>Sustainable Materials Cost Analysis</li>
        <li>Energy Modeling</li>
        <li>Mechanical System Options</li>
        <li>Carbon Advisory</li>
      </ul>
    </div>
    <div class="contact-mark">
      <div class="contact-mark__square"></div>
      <div class="contact-mark__name">Vanto</div>
    </div>
    <ul class="contact">
      <li><svg viewBox="0 0 10 10"><path d="M5 9.5C2.5 6 2 5 2 3.8a3 3 0 0 1 6 0C8 5 7.5 6 5 9.5z"/></svg>P.O. Box 4170, Marlow Bay, UAE</li>
      <li><svg viewBox="0 0 10 10"><rect x="1.5" y="4" width="7" height="5"/><path d="M1 3.5Q5 0 9 3.5"/></svg>+971 4 5550147</li>
      <li><svg viewBox="0 0 10 10"><rect x="1.5" y="4.5" width="7" height="4.5"/><rect x="3" y="1" width="4" height="3.5"/></svg>+971 4 5550148</li>
      <li><svg viewBox="0 0 10 10"><circle cx="5" cy="5" r="4"/><path d="M1 5h8M5 1c-2 2.5-2 5.5 0 8M5 1c2 2.5 2 5.5 0 8"/></svg>www.vanto-pm.com</li>
    </ul>
  </section>

  <section class="panel panel--front">
    <svg class="panel-art" width="700" height="908" viewBox="0 0 700 908">
      <defs>
        <linearGradient id="cityTone" x1="0" y1="0" x2="0.3" y2="1">
          <stop offset="0" stop-color="#d6d3bd"/>
          <stop offset="0.45" stop-color="#aab3ad"/>
          <stop offset="0.75" stop-color="#7f9a73"/>
          <stop offset="1" stop-color="#b9b39e"/>
        </linearGradient>
        <linearGradient id="webTab" x1="0" x2="1">
          <stop offset="0" stop-color="#bcd3ef"/><stop offset="1" stop-color="#eef4fb"/>
        </linearGradient>
      </defs>
      <polygon points="80,190 700,190 700,618 0,618 0,270" fill="url(#cityTone)" role="img" aria-label="Aerial 3D rendering of a master-planned city district with towers and parkland"/>
    </svg>
    <div class="front-mark">
      <div class="front-mark__square"></div>
      <div class="front-mark__name">Vanto</div>
      <div class="front-mark__desc">PROJECT MANAGEMENT</div>
    </div>
    <p class="tagline">YOUR VISION OUR EXPERTISE</p>
    <div class="web-tab">
      <svg width="270" height="45" viewBox="0 0 270 45"><polygon points="40,0 270,0 270,45 0,45" fill="url(#webTab)"/></svg>
      <span class="web-tab__text"><svg viewBox="0 0 10 10"><circle cx="5" cy="5" r="4"/><path d="M1 5h8M5 1c-2 2.5-2 5.5 0 8M5 1c2 2.5 2 5.5 0 8"/></svg>www.vanto-pm.com</span>
    </div>
  </section>
  <div class="fold-strip"></div>
</div>
</body>
</html>
```